Electrical company needs a brochure designed for electrical construction work

we need a brochure designed for our company BRONZEWAY ELECTRICAL INSTALLATIONS. we are a group of electricians working in the construction industry delivering electrical constructon services to builders and other clients in the commercial and Industrial working environments. we would like our logo to stand out with a dark theme and also give a professional fee.l we have a brief description of what we do and our experiences in a word doc i will provide it along with our logo design

Target Market(s)

builders for commercial and industrial construction projects

Industry/Entity Type

Electric Company

Font styles to use
Serif

Colors
0456a4
96b7d9
5c5c5c
757575
000000
aaaaaa
ec1f27
33a6d7
0493ce

Requirements
Must have
• a professional feel,
Nice to have
• some wording that makes us stand out and brings all the attention

```html
<!DOCTYPE html>
<html lang="en">
<head>
<meta charset="utf-8">
<title>Bronzeway Electrical Installations – Brochure</title>
<link rel="stylesheet" href="https://fonts.googleapis.com/css2?family=Oswald:wght@500;700&family=Open+Sans:wght@400;600;700&display=swap">
<style>
:root{
  --navy:#0456a4;
  --sky:#96b7d9;
  --grey-dark:#5c5c5c;
  --grey:#757575;
  --grey-light:#aaaaaa;
  --black:#000000;
  --red:#ec1f27;
  --cyan:#33a6d7;
  --blue:#0493ce;
  --page-dark:#141416;
  --page-mid:#232326;
  --stage:#e8e8e8;
}
*{box-sizing:border-box;margin:0;padding:0}
html,body{width:859px;height:1200px;overflow:hidden}
body{background:var(--stage);font-family:"Open Sans",Arial,sans-serif;color:#d6d6d6;position:relative}
.spread{position:absolute;left:28px;width:803px;height:572px;overflow:hidden;
  background:linear-gradient(160deg,var(--page-mid),var(--page-dark) 60%);box-shadow:0 2px 8px rgba(0,0,0,.35)}
.spread--outer{top:18px}
.spread--inner{top:610px}
.spread svg.deco{position:absolute;inset:0;width:803px;height:572px}
.page{position:absolute;top:0;width:401.5px;height:572px}
.page--left{left:0}
.page--right{left:401.5px}
.fold{position:absolute;left:401px;top:0;width:1px;height:572px;background:rgba(0,0,0,.5)}
.photo{position:absolute}
.body-copy{font-size:6px;line-height:9px;color:#cfcfcf;text-align:justify}
.body-copy p+p{margin-top:6px}
.brand{display:flex;align-items:center;gap:7px}
.brand__dot{width:22px;height:22px;border-radius:50%;background:var(--cyan);flex:none}
.brand__name{font-family:"Oswald",Arial,sans-serif;font-weight:700;color:#fff;line-height:1;text-transform:uppercase}
.brand--lg .brand__name{font-size:30px}
.brand--lg .brand__name span{display:block;font-size:10px;letter-spacing:1.5px;margin-top:2px}
.brand--md .brand__dot{width:16px;height:16px}
.brand--md .brand__name{font-size:20px}
.brand--md .brand__name span{display:block;font-size:7px;letter-spacing:1px;margin-top:1px}
.tagline{font-family:"Oswald",Arial,sans-serif;font-weight:500;font-size:8px;letter-spacing:.6px;color:#e5e5e5;text-transform:uppercase}
.contact-bar{position:absolute;bottom:0;width:401.5px;height:30px;background:#0c0c0d;display:flex;align-items:center;justify-content:space-between;padding:0 18px;
  font-family:"Oswald",Arial,sans-serif;font-size:8px;letter-spacing:.4px}
.contact-bar__call{color:var(--red);font-weight:700}
.contact-bar__web{color:#e5e5e5;font-weight:500}
.section-title{font-family:"Oswald",Arial,sans-serif;font-weight:700;font-size:9px;color:var(--cyan);letter-spacing:.4px;text-transform:uppercase}
.service-list{display:grid;grid-template-columns:1fr 1fr;column-gap:12px;list-style:none;font-size:6px;line-height:9px;color:#d0d0d0}
.service-list li::before{content:"• ";color:var(--red)}
.sign-off{font-size:6px;line-height:9px;color:#cfcfcf}
</style>
</head>
<body>

<!-- Outer spread: back + cover -->
<section class="spread spread--outer">
  <svg class="deco" viewBox="0 0 803 572" aria-hidden="false">
    <defs>
      <linearGradient id="hall" x1="0" y1="0" x2="0" y2="1">
        <stop offset="0" stop-color="#c9d3dc"/>
        <stop offset=".55" stop-color="#9aa6b1"/>
        <stop offset="1" stop-color="#d9dee2"/>
      </linearGradient>
    </defs>
    <polygon points="0,0 803,0 803,262 401,150 0,108" fill="url(#hall)" role="img" aria-label="Photo of a large lit industrial warehouse interior"/>
    <polygon points="0,108 401,150 803,262 803,282 401,168 0,124" fill="var(--blue)"/>
    <polygon points="0,124 401,168 803,282 803,286 401,172 0,128" fill="var(--red)"/>
    <polygon points="0,470 401,505 401,520 0,488" fill="var(--blue)"/>
    <polygon points="0,488 401,520 401,523 0,491" fill="var(--cyan)"/>
    <polygon points="401,440 803,470 803,490 401,456" fill="var(--blue)"/>
  </svg>

  <div class="page page--left">
    <div class="body-copy" style="position:absolute;left:28px;top:150px;width:345px">
      <p>Bronzeway Electrical Installations is a team of licensed electricians delivering electrical construction services to builders across commercial and industrial sites. From first fix to final commissioning, we plan, install and test every circuit to the standards your project demands, on time and on budget.</p>
      <p>Our crews work alongside site managers and trades to keep programs moving. We handle switchboards, lighting, power distribution, data cabling and machine connections, with clear reporting at every stage.</p>
      <p>Safety is built into everything we do. Every installation is documented, certified and backed by our workmanship guarantee so you can hand over with confidence.</p>
    </div>
    <div class="contact-bar">
      <span class="contact-bar__call">CALL DALE MORROW T: 0400 555 218</span>
      <span class="contact-bar__web">BRONZEWAYELECTRICAL.COM.AU</span>
    </div>
  </div>

  <div class="page page--right">
    <div class="brand brand--lg" style="position:absolute;left:70px;top:308px">
      <div class="brand__dot"></div>
      <div class="brand__name">Bronzeway<span>Electrical Installations</span></div>
    </div>
    <div class="tagline" style="position:absolute;left:0;width:401.5px;top:370px;text-align:center">Electrical Construction &amp; Industrial Construction Work</div>
    <div class="contact-bar">
      <span class="contact-bar__call">CALL DALE MORROW T: 0400 555 218</span>
      <span class="contact-bar__web">BRONZEWAYELECTRICAL.COM.AU</span>
    </div>
  </div>
  <div class="fold"></div>
</section>

<!-- Inner spread -->
<section class="spread spread--inner">
  <svg class="deco" viewBox="0 0 803 572">
    <polygon points="0,392 401,420 401,434 0,404" fill="var(--blue)"/>
    <polygon points="0,404 401,434 401,437 0,407" fill="var(--red)"/>
    <polygon points="0,407 401,437 401,572 0,572" fill="#b9a590" role="img" aria-label="Photos of an electrician's hands stripping cable and of a modern fitted-out office"/>
    <polygon points="160,421 401,437 401,572 250,572" fill="#c9cdd2"/>
    <polygon points="401,0 803,0 803,200 401,240" fill="#6f8193" role="img" aria-label="Photos of an electrician testing a switchboard and of cable installation on site"/>
    <polygon points="600,0 803,0 803,200 600,220" fill="#8a97a2"/>
    <polygon points="401,240 803,200 803,214 401,254" fill="var(--blue)"/>
    <polygon points="401,254 803,214 803,217 401,257" fill="var(--cyan)"/>
  </svg>

  <div class="page page--left">
    <div class="brand brand--md" style="position:absolute;left:100px;top:22px">
      <div class="brand__dot"></div>
      <div class="brand__name">Bronzeway<span>Electrical Installations</span></div>
    </div>
    <div class="body-copy" style="position:absolute;left:28px;top:78px;width:345px">
      <p>Bronzeway Electrical Installations brings years of hands-on site experience to every build. We partner with builders to deliver reliable power systems for warehouses, offices, retail fit-outs and industrial plants.</p>
    </div>
    <div class="section-title" style="position:absolute;left:28px;top:190px">Commercial &amp; Industrial Projects</div>
    <ul class="service-list" style="position:absolute;left:28px;top:208px;width:345px">
      <li>Main switchboard installation</li>
      <li>Sub-board and distribution</li>
      <li>Commercial lighting systems</li>
      <li>Emergency and exit lighting</li>
      <li>Industrial machine connections</li>
      <li>Data and communications cabling</li>
      <li>Power and outlet layouts</li>
      <li>Cable tray and conduit</li>
      <li>Testing and commissioning</li>
      <li>Three phase power</li>
      <li>Site temporary power</li>
      <li>Maintenance and upgrades</li>
    </ul>
  </div>

  <div class="page page--right">
    <div class="brand brand--md" style="position:absolute;left:110px;top:280px">
      <div class="brand__dot"></div>
      <div class="brand__name">Bronzeway<span>Electrical Installations</span></div>
    </div>
    <div class="body-copy" style="position:absolute;left:28px;top:340px;width:345px">
      <p>We believe every project deserves a partner who answers the phone, turns up on time and finishes the job right. Talk to us about your next build and let our team power it from the ground up.</p>
    </div>
    <div class="sign-off" style="position:absolute;left:28px;top:400px;width:345px">
      <p>Thank you, we look forward to working with you.</p>
      <p>Kind regards,</p>
      <p>Dale Morrow</p>
      <p>Bronzeway Electrical</p>
      <p>dale@bronzewayelectrical.com.au</p>
    </div>
  </div>
  <div class="fold"></div>
</section>

</body>
</html>
```